Holvery Real Estate Management Consulting

To design a high end company profile that inspires confidence in high net worth individuals and similar clients. The profile to include real estate images, preferably real images. The firm is a Zambian firm and has its target to be comparable to Tesk & Company, Parlowe & Company, Wilder Osten, Lun dorv pelsin wilder osten, TLAV Real estate company as such.

Target Market(s)

Real estate clients such as high net worth individuals, private and public companies, government and international agencies, banks and insurance companies, trusts and pension funds and individual investors. the sub target market group being developers, planners, financiers, market analysts, designers, economists, engineers, architects, construction managers, quantity surveyors and public officials and others

Colors

Designer to choose colors to be used in the design.

Requirements
Must have
• Company logo

```html
<!DOCTYPE html>
<html lang="en">
<head>
<meta charset="utf-8">
<title>Holvery Real Estate – Company Profile</title>
<link rel="stylesheet" href="https://fonts.googleapis.com/css2?family=Montserrat:wght@200;300;400;600;800;900&family=Roboto+Condensed:wght@400;700&display=swap">
<style>
  :root {
    --bg: #2b2b2b;
    --brand-blue: #2e4aa6;
    --deep-blue: #1f3c9c;
    --band-blue: #3a50a3;
    --ink: #333333;
    --muted: #4a4a4a;
    --paper: #ffffff;
    --rule: #8a8a8a;
    --accent-edge: #b86a3a;
    --sky-top: #1f45b2;
    --sky-low: #2f62cc;
    --facade-warm: #b8793f;
    --facade-deep: #6b4530;
    --street: #8d9099;
  }
  * { margin: 0; padding: 0; box-sizing: border-box; }
  html, body { width: 1200px; height: 903px; overflow: hidden; }
  body { background: var(--bg); position: relative; font-family: "Montserrat", sans-serif; }

  .page { position: absolute; top: 147px; width: 422px; height: 562px; overflow: hidden; border: 1px solid var(--accent-edge); }
  .cover { left: 114px; background: linear-gradient(180deg, var(--sky-top) 0%, var(--sky-low) 100%); }
  .inner { left: 656px; background: var(--paper); }

  /* Cover */
  .cover-brand { position: absolute; top: 46px; left: 210px; width: 140px; text-align: center; color: var(--paper); font-weight: 800; font-size: 34px; letter-spacing: 1px; line-height: 40px; }
  .cover-title { position: absolute; top: 104px; right: 11px; color: var(--paper); }
  .cover-title .line-strong { font-weight: 900; font-size: 17.5px; letter-spacing: 0.2px; line-height: 20px; }
  .cover-title .line-light { font-weight: 200; font-size: 17.5px; letter-spacing: 0.5px; line-height: 22px; }
  .cover-photo { position: absolute; top: 152px; left: 0; width: 422px; height: 352px;
    background: linear-gradient(180deg, var(--sky-low) 0%, #3a55a0 14%, var(--facade-deep) 34%, var(--facade-warm) 58%, #a86f3c 78%, #5e4a40 92%, var(--street) 100%); }
  .cover-band { position: absolute; left: 0; bottom: 0; width: 422px; height: 60px; }
  .cover-tagline { position: absolute; left: 26px; bottom: 22px; color: var(--paper); font-family: "Roboto Condensed", sans-serif; font-weight: 700; font-size: 20px; letter-spacing: 0.3px; }

  /* Inner */
  .title-bar { position: absolute; top: 23px; left: 0; width: 325px; height: 19px; background: var(--brand-blue); color: var(--paper); font-family: "Roboto Condensed", sans-serif; font-weight: 700; font-size: 15px; line-height: 19px; padding-left: 22px; }
  .inner-brand { position: absolute; top: 23px; left: 338px; color: var(--deep-blue); font-weight: 800; font-size: 14px; line-height: 19px; letter-spacing: 0.5px; }
  .heading { position: absolute; color: var(--deep-blue); font-family: "Roboto Condensed", sans-serif; font-weight: 700; font-size: 11.5px; }
  .who-heading { top: 55px; left: 22px; }
  .body-text { position: absolute; color: var(--muted); font-size: 7px; line-height: 9.3px; font-weight: 400; text-align: justify; }
  .who-text { top: 75px; left: 22px; width: 378px; }

  .services { position: absolute; top: 130px; left: 22px; width: 223px; height: 280px; border: 1px solid var(--rule); border-radius: 2px; overflow: hidden; }
  .services-head { height: 26px; background: var(--brand-blue); color: var(--paper); font-weight: 600; font-size: 7px; line-height: 8.5px; position: relative; }
  .services-head .col-a { position: absolute; left: 4px; top: 4px; }
  .services-head .col-b { position: absolute; left: 78px; top: 9px; }
  .service-row { position: relative; border-bottom: 1px solid var(--rule); font-size: 7.2px; line-height: 9.3px; color: var(--ink); }
  .service-row:last-child { border-bottom: none; }
  .service-row .label { position: absolute; left: 4px; }
  .service-row .scope { position: absolute; left: 66px; }
  .row-consulting { height: 93px; }
  .row-consulting .label, .row-consulting .scope { top: 9px; }
  .row-valuations { height: 104px; }
  .row-valuations .label, .row-valuations .scope { top: 7px; }
  .row-reference { height: 55px; }
  .row-reference .label { top: 14px; }
  .row-reference .scope { top: 6px; }

  .solutions-heading { top: 134px; left: 264px; }
  .solutions-text { top: 152px; left: 264px; width: 136px; font-size: 7.1px; }

  .address-heading { position: absolute; top: 432px; left: 22px; color: var(--deep-blue); font-weight: 600; font-size: 7.5px; }
  .address-text { position: absolute; top: 453px; left: 22px; color: var(--ink); font-size: 7px; line-height: 9.3px; font-style: normal; }

  .handshake-photo { position: absolute; top: 416px; left: 222px; width: 200px; height: 146px;
    background: linear-gradient(90deg, rgba(255,255,255,1) 0%, rgba(220,230,242,0.9) 22%, #c7d6e8 50%, #e9cdb8 75%, #b9cde2 100%); }
  .inner-band { position: absolute; left: 0; bottom: 0; width: 422px; height: 38px; }
  .website { position: absolute; left: 28px; bottom: 12px; color: var(--paper); font-size: 9px; font-weight: 400; }
</style>
</head>
<body>
  <section class="page cover">
    <div class="cover-brand">HOLVERY</div>
    <div class="cover-title">
      <div class="line-strong">MANAGEMENT CONSULTING</div>
      <div class="line-light">HOLVERY REAL ESTATE</div>
    </div>
    <div class="cover-photo" role="img" aria-label="Photograph of a modern apartment building lit up at dusk"></div>
    <svg class="cover-band" viewBox="0 0 422 60" aria-hidden="true">
      <polygon points="0,0 262,0 300,60 0,60" fill="var(--band-blue)"/>
      <polygon points="262,0 272,0 318,34 422,34 422,40 306,40" fill="#d9d9d9"/>
      <polygon points="300,60 306,40 422,40 422,60" fill="var(--band-blue)"/>
    </svg>
    <div class="cover-tagline">ACCELERATE SUCCESS....</div>
  </section>

  <section class="page inner">
    <div class="title-bar">INSPIRE VALUE</div>
    <div class="inner-brand">HOLVERY</div>

    <h2 class="heading who-heading">WHO WE ARE</h2>
    <p class="body-text who-text">HRE | Management Consulting is one of Zambia`s leading professional real estate services firms with an outstanding reputation and has its cornerstone the excellence of its people. Since its inception, the business has continued successfully with a national client base, a number of which have retained our services.</p>

    <div class="services">
      <div class="services-head"><span class="col-a">CORE<br>SERVICES</span><span class="col-b">SCOPE</span></div>
      <div class="service-row row-consulting">
        <span class="label">Consulting</span>
        <span class="scope">Advisory Services<br>Acquisition, Leasing &amp; Disposal Advise<br>Business Plans<br>Feasibility studies<br>Highest and Best Use Studies<br>Market research/analysis<br>Planning and development<br>Property Condition Assessments</span>
      </div>
      <div class="service-row row-valuations">
        <span class="label">Valuations</span>
        <span class="scope">Agriculture Valuations<br>Asset Valuations<br>Commercial Valuations<br>Leisure/Hotels/Lodges<br>Industrial Valuations<br>Special purpose Valuations<br>Mines Valuations<br>Residential Valuations<br>Plant, Machinery &amp; Equipment</span>
      </div>
      <div class="service-row row-reference">
        <span class="label">Firm's<br>Reference</span>
        <span class="scope">The Property Valuers Registration<br>Council<br>P.O Box 41180<br>Lusaka</span>
      </div>
    </div>

    <h2 class="heading solutions-heading">Our Solutions</h2>
    <p class="body-text solutions-text">As a preferred property firm we continually monitor property value levels and will provide you with an update on market rents, trends and the position of your property in the marketplace. We continue to roll out our real estate services for you our clients to benefit from the power of our massive experience and database. Our system allows you to save on unnecessary research costs &amp; time of doing new research in the marketplace and all due diligence is done when identifying the interests, benefits and rights being researched. We assure our clients &amp; prospective clients that our work is independent, objective and compliant with nationally recognized Laws of the Republic of Zambia.</p>

    <div class="address-heading">Our address is as follows:</div>
    <address class="address-text">Messrs. HRE | Management Consulting<br>Unit 4, Plot NO. 2217<br>Meridian Road<br>Kafue, Lusaka Province– Zambia<br>Mobile: +260 900 000 111/ 0900 222333<br>E-mail: info@holverypropertyconsultants.com</address>

    <div class="handshake-photo" role="img" aria-label="Photograph of a business handshake above a small model house, keys and documents"></div>
    <svg class="inner-band" viewBox="0 0 422 38" aria-hidden="true">
      <polygon points="0,0 248,0 270,38 0,38" fill="var(--band-blue)"/>
      <polygon points="248,0 256,0 280,28 422,28 422,32 274,32" fill="#cfd6e6"/>
    </svg>
    <div class="website">www.holverypropertyconsultants.com</div>
  </section>
</body>
</html>
```